Lending Harbor Partners - business cards

we need new business cards for my company.
i've been in business for 25 years.
my wife and I are mortgage brokers.

we just bought the domain for a website with www.homekeyfunding.example
that could be used in the design also.

On the business card would be
Front card:

Dale Whitcomb
Owner/Loan Officer
Cell: (555) 314-2297
Lending Harbor Partners
4172 Pinecrest Lane
Cedar Valley, CA 94021
Office (555) 490-6631
Fax (555) 490-6674
website www.homekeyfunding.example

Back of Card:

LHP BRE #0378215 NMLS #586249
Dale Whitcomb BRE # 04519863 NMLS #587716

Industry/Entity Type

Business

```html
<!DOCTYPE html>
<html lang="en">
<head>
<meta charset="utf-8">
<title>Lending Harbor Partners – Business Cards</title>
<link rel="stylesheet" href="https://fonts.googleapis.com/css2?family=Ubuntu:wght@400;500;700&display=swap">
<style>
  :root {
    --page-bg: #ececec;
    --card-white: #ffffff;
    --brand-brown: #5a3129;
    --brand-blue: #16a1db;
    --text-light: #eadcd6;
    --text-grey: #8a8a8a;
    --text-dark: #1d2b36;
  }
  * { box-sizing: border-box; margin: 0; padding: 0; }
  html, body { width: 1200px; height: 1200px; overflow: hidden; }
  body {
    background: var(--page-bg);
    font-family: "Ubuntu", sans-serif;
    position: relative;
  }
  .card {
    position: absolute;
    left: 180px;
    width: 840px;
    height: 480px;
    overflow: hidden;
    box-shadow: 0 10px 30px rgba(0,0,0,0.15);
  }
  .brand-name {
    color: #ffffff;
    font-weight: 700;
    line-height: 1.05;
    display: flex;
    align-items: center;
    gap: 16px;
  }
  .brand-mark {
    width: 44px; height: 44px;
    background: var(--brand-blue);
    flex: none;
  }

  /* Back card */
  .card-back { top: 60px; background: var(--card-white); }
  .card-back .brand-band {
    position: absolute;
    left: 0; top: 70px;
    width: 640px; height: 150px;
    background: var(--brand-brown);
    display: flex; align-items: center;
    padding-left: 70px;
  }
  .card-back .brand-name { font-size: 40px; }
  .licences {
    position: absolute;
    left: 190px; top: 248px;
    color: var(--text-grey);
    font-size: 22px;
    line-height: 1.3;
  }

  /* Front card */
  .card-front { top: 640px; background: var(--brand-brown); }
  .edge-tab {
    position: absolute; left: 0; top: 60px;
    width: 60px; height: 70px;
    background: var(--brand-blue);
  }
  .card-front .brand-name {
    position: absolute; left: 110px; top: 58px;
    font-size: 32px;
  }
  .name-band {
    position: absolute; left: 350px; top: 140px;
    right: 0; height: 120px;
    background: var(--brand-blue);
    padding: 14px 0 0 30px;
    color: var(--text-dark);
  }
  .person-name { font-size: 30px; font-weight: 700; }
  .person-title { font-size: 21px; margin-top: 2px; }
  .contact-line {
    display: flex; align-items: center; gap: 8px;
    font-size: 21px; margin-top: 2px;
  }
  .icon { width: 20px; height: 20px; flex: none; }
  .details {
    position: absolute; left: 380px; top: 280px;
    color: var(--text-light);
    font-size: 21px;
    line-height: 1.3;
  }
  .details .address { margin-bottom: 12px; }
</style>
</head>
<body>

<section class="card card-back" aria-label="Back of business card">
  <div class="brand-band">
    <div class="brand-name"><span class="brand-mark"></span>Lending Harbor<br>Partners</div>
  </div>
  <div class="licences">
    <p>LHP BRE #0378215</p>
    <p>NMLS #586249</p>
    <p>Dale Whitcomb BRE # 04519863</p>
    <p>NMLS #587716</p>
  </div>
</section>

<section class="card card-front" aria-label="Front of business card">
  <div class="edge-tab"></div>
  <div class="brand-name"><span class="brand-mark"></span>Lending Harbor<br>Partners</div>

  <div class="name-band">
    <p class="person-name">Dale Whitcomb</p>
    <p class="person-title">Owner/Loan Officer</p>
    <p class="contact-line">
      <svg class="icon" viewBox="0 0 20 20" aria-hidden="true"><rect width="20" height="20" rx="3" fill="#e4572e"/><rect x="6" y="3" width="8" height="14" rx="1.5" fill="none" stroke="#fff" stroke-width="1.6"/><circle cx="10" cy="14.5" r="0.9" fill="#fff"/></svg>
      (555) 314-2297
    </p>
  </div>

  <div class="details">
    <div class="address">
      <p>4172 Pinecrest Lane</p>
      <p>Cedar Valley, CA 94021</p>
    </div>
    <p class="contact-line">
      <svg class="icon" viewBox="0 0 20 20" aria-hidden="true"><rect width="20" height="20" rx="3" fill="var(--brand-blue)"/><path d="M6 4c1 0 2 3 1.5 3.5L6.5 8.5c1 2 3 4 5 5l1-1c.5-.5 3.5.5 3.5 1.5v1.5c0 .5-1 1-2 1C9 16.5 3.5 11 3.5 6c0-1 .5-2 1-2z" fill="#fff"/></svg>
      (555) 490-6631
    </p>
    <p class="contact-line">
      <svg class="icon" viewBox="0 0 20 20" aria-hidden="true"><rect width="20" height="20" rx="3" fill="var(--brand-blue)"/><rect x="4" y="8" width="12" height="7" rx="1" fill="#fff"/><rect x="6.5" y="4" width="7" height="4" fill="#fff"/></svg>
      (555) 490-6674
    </p>
    <p class="contact-line">
      <svg class="icon" viewBox="0 0 20 20" aria-hidden="true"><rect width="20" height="20" rx="3" fill="var(--brand-blue)"/><circle cx="10" cy="10" r="5.5" fill="none" stroke="#fff" stroke-width="1.4"/><path d="M4.5 10h11M10 4.5c-2.5 3-2.5 8 0 11M10 4.5c2.5 3 2.5 8 0 11" fill="none" stroke="#fff" stroke-width="1.1"/></svg>
      www.homekeyfunding.example
    </p>
  </div>
</section>

</body>
</html>
```